table invoices in a modern format! (make it fun to look at!!)

Our has invoices that are shown to our clients. This is currently done in a normal table view, but its boring to look at and is not modern.
We would like to have a modern look and feel
it should ABSOLUTLY not be in table form.
Cards, graphs, pictures, whatever... should be fun and almost interactive.

the table file is how it current looks like.
the other two files were "ideas" to have a better representation
IT DOES NOT NEED TO LOOK LIKE THAT if you have a better idea please go for it.

secondary objective, the graphs/cards/whatever you design should be interactive, meaning I can "click on it" to pay a bill, or see more info.

Let me know if there are more questions!

```html
<!DOCTYPE html>
<html lang="en">
<head>
<meta charset="utf-8">
<title>LedgerTile – Invoices Dashboard</title>
<link href="https://fonts.googleapis.com/css2?family=Roboto:wght@400;500;700&display=swap" rel="stylesheet">
<style>
:root{
  --backdrop:#a6a6a6;
  --sidebar:#262f3e;
  --sidebar-top:#2c3646;
  --sidebar-active:#1c2330;
  --sidebar-line:#1f2733;
  --sidebar-text:#aab4c2;
  --accent:#3fb6ea;
  --main-bg:#eef3fa;
  --panel:#ffffff;
  --panel-head:#f6f8fb;
  --border:#e1e7ef;
  --ink:#3a3f48;
  --muted:#9aa3ae;
  --blue-btn:#0b6fc5;
  --green-btn:#1eb30e;
  --paid:#17a00f;
  --partial:#f8a900;
  --unpaid:#e8120c;
  --tip:#4c5a6b;
  --area-blue:#6fcaf0;
  --mint:#36f0b5;
  --violet:#b24cf5;
  --pdf:#d60d0d;
}
*{box-sizing:border-box;margin:0;padding:0}
html,body{width:1200px;height:1200px;overflow:hidden;background:var(--backdrop);font-family:'Roboto',sans-serif;color:var(--ink)}
.stage{position:absolute;left:0;top:0;width:1800px;height:1800px;transform:scale(.666667);transform-origin:0 0}
.abs{position:absolute}
.app{left:198px;top:58px;width:1370px;height:1675px;background:var(--main-bg)}
.sidebar{left:198px;top:58px;width:270px;height:1675px;background:var(--sidebar)}
.brand{left:198px;top:58px;width:270px;height:90px;background:var(--sidebar-top);display:flex;align-items:center;justify-content:center;color:var(--accent);font-size:27px;font-weight:500;letter-spacing:.5px}
.year{left:198px;width:270px;height:60px;border-bottom:1px solid var(--sidebar-line);display:flex;align-items:center;padding-left:44px;color:var(--sidebar-text);font-size:15px;gap:22px}
.year.active{background:var(--sidebar-active);color:var(--accent);height:54px}
.year.active::before{content:"";position:absolute;left:0;top:19px;border:8px solid transparent;border-left-color:var(--accent);border-left-width:7px}
.year svg{width:18px;height:18px}
.side-foot{left:198px;top:1686px;width:270px;border-top:1px solid #344052;padding-top:18px;text-align:center;font-size:12px;color:#6f7a89}
.topbar{left:468px;top:58px;width:1100px;height:90px;background:#fff}
.search{left:596px;top:92px;font-size:17px;color:#c3c9d1}
.user{left:1262px;top:82px;width:162px;height:34px;border-radius:17px;background:#eef3f8}
.avatar{left:1262px;top:76px;width:46px;height:46px;border-radius:50%;background:radial-gradient(circle at 50% 40%,#f5c89a,#e2a35f 55%,#3c4a5e 56%)}
.user-name{left:1317px;top:95px;font-size:12px;font-weight:500;color:#2b3340}
.overview{left:1435px;top:88px;width:113px;height:28px;border-radius:14px;background:var(--accent);color:#fff;font-size:12px;display:flex;align-items:center;justify-content:center}
.page-title{left:488px;top:160px;font-size:24px;font-weight:500;color:#2f3540}
.stat{top:202px;width:249px;height:94px;background:#fff;border:1px solid var(--border);display:flex}
.stat .ico{width:70px;border-right:1px solid var(--border);background:#fafcfe;display:flex;align-items:flex-start;justify-content:center;padding-top:18px}
.stat .val{padding:20px 0 0 20px}
.stat .amount{font-size:24px;color:#4a505a}
.stat .label{font-size:14px;color:var(--muted);margin-top:6px}
.btn{left:1297px;width:248px;height:41px;border-radius:21px;color:#fff;font-size:19px;font-weight:500;display:flex;align-items:center;justify-content:center}
.panel{background:var(--panel);border:1px solid var(--border)}
.panel-head{position:absolute;left:0;top:0;right:0;height:48px;background:var(--panel-head);border-bottom:1px solid var(--border);display:flex;align-items:center;padding-left:20px;font-size:16px;font-weight:500;color:#3a3f48;letter-spacing:.3px}
.small{font-size:12px;color:#4a505a;font-weight:400}
.badge{height:23px;color:#fff;font-size:14px;display:flex;align-items:center;justify-content:center}
.b-paid{background:var(--paid)}.b-partial{background:var(--partial)}.b-unpaid{background:var(--unpaid)}
.tag{height:30px;color:#fff;font-size:16px;font-weight:700;display:flex;align-items:center;justify-content:center}
.month{font-size:14px;color:#4a505a;letter-spacing:.4px;transform:translateX(-50%)}
.nav{width:29px;height:28px;border:1px solid #d6dde6;background:#fff;color:var(--accent);font-size:14px;display:flex;align-items:center;justify-content:center}
.big{font-size:30px;color:#2aa7e0}
.legend{font-size:12px;letter-spacing:.4px;display:flex;align-items:center;gap:9px}
.legend i{width:9px;height:9px;display:inline-block}
.wallet-legend{font-size:13px;color:#2f3540;display:flex;gap:6px;align-items:center}
.wallet-legend i{width:11px;height:11px;display:inline-block}
.axis{font-size:11px;color:#5a626e;font-weight:500}
.ylab{font-size:14px;color:#2aa7e0}
</style>
</head>
<body>
<div class="stage">
  <div class="abs app"></div>

  <!-- Sidebar -->
  <nav class="abs sidebar"></nav>
  <div class="abs brand">LedgerTile</div>
  <div class="abs year active" style="top:148px"><svg viewBox="0 0 18 18"><rect x="1" y="3" width="16" height="14" fill="none" stroke="currentColor" stroke-width="1.6"/><path d="M1 7h16M5 1v4M13 1v4M4 10h2M8 10h2M12 10h2M4 13h2M8 13h2M12 13h2" stroke="currentColor" stroke-width="1.4"/></svg>2019</div>
  <div class="abs year" style="top:205px"><svg viewBox="0 0 18 18"><rect x="1" y="3" width="16" height="14" fill="none" stroke="#3fb6ea" stroke-width="1.6"/><path d="M1 7h16M5 1v4M13 1v4M4 10h2M8 10h2M12 10h2M4 13h2M8 13h2M12 13h2" stroke="#3fb6ea" stroke-width="1.4"/></svg>2020</div>
  <div class="abs year" style="top:265px"><svg viewBox="0 0 18 18"><rect x="1" y="3" width="16" height="14" fill="none" stroke="#3fb6ea" stroke-width="1.6"/><path d="M1 7h16M5 1v4M13 1v4M4 10h2M8 10h2M12 10h2M4 13h2M8 13h2M12 13h2" stroke="#3fb6ea" stroke-width="1.4"/></svg>2021</div>
  <div class="abs year" style="top:325px"><svg viewBox="0 0 18 18"><rect x="1" y="3" width="16" height="14" fill="none" stroke="#3fb6ea" stroke-width="1.6"/><path d="M1 7h16M5 1v4M13 1v4M4 10h2M8 10h2M12 10h2M4 13h2M8 13h2M12 13h2" stroke="#3fb6ea" stroke-width="1.4"/></svg>2022</div>
  <div class="abs year" style="top:385px"><svg viewBox="0 0 18 18"><rect x="1" y="3" width="16" height="14" fill="none" stroke="#3fb6ea" stroke-width="1.6"/><path d="M1 7h16M5 1v4M13 1v4M4 10h2M8 10h2M12 10h2M4 13h2M8 13h2M12 13h2" stroke="#3fb6ea" stroke-width="1.4"/></svg>2023</div>
  <div class="abs year" style="top:445px"><svg viewBox="0 0 18 18"><rect x="1" y="3" width="16" height="14" fill="none" stroke="#3fb6ea" stroke-width="1.6"/><path d="M1 7h16M5 1v4M13 1v4M4 10h2M8 10h2M12 10h2M4 13h2M8 13h2M12 13h2" stroke="#3fb6ea" stroke-width="1.4"/></svg>2024</div>
  <div class="abs year" style="top:505px;border-bottom:none"><svg viewBox="0 0 18 18"><rect x="1" y="3" width="16" height="14" fill="none" stroke="#3fb6ea" stroke-width="1.6"/><path d="M1 7h16M5 1v4M13 1v4M4 10h2M8 10h2M12 10h2M4 13h2M8 13h2M12 13h2" stroke="#3fb6ea" stroke-width="1.4"/></svg>2025</div>
  <div class="abs side-foot">© 2019 LEDGERTILE</div>

  <!-- Top bar -->
  <header class="abs topbar"></header>
  <svg class="abs" style="left:488px;top:92px" width="22" height="20" viewBox="0 0 22 20"><path d="M1 3h20M1 10h20M1 17h20" stroke="#3fb6ea" stroke-width="2"/></svg>
  <svg class="abs" style="left:551px;top:90px" width="26" height="26" viewBox="0 0 26 26"><circle cx="15" cy="11" r="8" fill="none" stroke="#c3c9d1" stroke-width="1.6"/><path d="M9 17L2 24" stroke="#c3c9d1" stroke-width="1.8"/></svg>
  <div class="abs search">Search..</div>
  <div class="abs user"></div>
  <div class="abs avatar" role="img" aria-label="User profile photo"></div>
  <div class="abs user-name">John Doe</div>
  <svg class="abs" style="left:1402px;top:98px" width="10" height="8" viewBox="0 0 10 8"><path d="M1 2l4 4 4-4" fill="none" stroke="#3fb6ea" stroke-width="1.5"/></svg>
  <div class="abs overview">Year Overview</div>

  <h1 class="abs page-title">Invoices Prior to 2019</h1>

  <!-- Stat cards -->
  <div class="abs stat" style="left:488px"><div class="ico"><svg width="32" height="32" viewBox="0 0 32 32"><circle cx="16" cy="17" r="13" fill="none" stroke="#3fb6ea" stroke-width="1.4"/><path d="M16 17V4M16 17L4 21" stroke="#3fb6ea" stroke-width="1.4"/></svg></div><div class="val"><div class="amount">$32300</div><div class="label">Payment</div></div></div>
  <div class="abs stat" style="left:758px"><div class="ico"><svg width="32" height="32" viewBox="0 0 32 32"><rect x="3" y="7" width="22" height="22" fill="none" stroke="#3fb6ea" stroke-width="1.4"/><rect x="3" y="17" width="12" height="12" fill="none" stroke="#3fb6ea" stroke-width="1.4"/><path d="M17 15L29 3M21 3h8v8" fill="none" stroke="#3fb6ea" stroke-width="1.4"/></svg></div><div class="val"><div class="amount">$16500</div><div class="label">Total Price</div></div></div>
  <div class="abs stat" style="left:1028px"><div class="ico"><svg width="32" height="32" viewBox="0 0 32 32"><path d="M8 3h16M8 29h16M10 3c0 9 12 9 12 13s-12 4-12 13M22 3c0 9-12 9-12 13s12 4 12 13" fill="none" stroke="#3fb6ea" stroke-width="1.4"/></svg></div><div class="val"><div class="amount">$22700</div><div class="label">Total Balance</div></div></div>
  <div class="abs btn" style="top:203px;background:var(--blue-btn)">Move To Wallet</div>
  <div class="abs btn" style="top:256px;background:var(--green-btn)">Pay a Bill</div>

  <!-- Open balance panel -->
  <section class="abs panel" style="left:488px;top:318px;width:1059px;height:482px">
    <div class="panel-head">MONTH OF OPEN BALANCE</div>
  </section>
  <svg class="abs" style="left:1082px;top:331px" width="20" height="20" viewBox="0 0 20 20"><circle cx="10" cy="10" r="7.5" fill="#fff" stroke="#4c5a6b" stroke-width="4"/></svg>
  <div class="abs small" style="left:1115px;top:333px;font-size:14px">Open Balance</div>
  <div class="abs small" style="left:1251px;top:335px">01/01/2019</div>
  <svg class="abs" style="left:1328px;top:339px" width="10" height="6"><path d="M0 0h10L5 6z" fill="#3fb6ea"/></svg>
  <div class="abs small" style="left:1378px;top:335px;color:#9aa3ae">to</div>
  <div class="abs small" style="left:1433px;top:335px">31/12/2019</div>
  <svg class="abs" style="left:1509px;top:339px" width="10" height="6"><path d="M0 0h10L5 6z" fill="#3fb6ea"/></svg>

  <svg class="abs" style="left:0;top:0" width="1800" height="800" viewBox="0 0 1800 800">
    <defs><linearGradient id="blueArea" x1="0" y1="0" x2="0" y2="1"><stop offset="0" stop-color="#6fcaf0"/><stop offset="1" stop-color="#6fcaf0" stop-opacity=".08"/></linearGradient></defs>
    <g stroke="#e3e8ee" stroke-dasharray="4 4"><path d="M558 416H1527M558 466H1527M558 566H1527M558 616H1527"/></g>
    <path d="M558 666H1527M558 550V666" stroke="#dfe5ec"/>
    <path d="M558 550L680 537L800 468L922 456L1047 496L1165 462L1293 475L1405 436L1527 445V666H558Z" fill="url(#blueArea)"/>
    <path d="M558 550L680 537L800 468L922 456L1047 496L1165 462L1293 475L1405 436L1527 445" fill="none" stroke="#3fb6ea" stroke-width="1.6"/>
    <path d="M558 516H1527" stroke="#3fb6ea" stroke-dasharray="4 3"/>
    <circle cx="922" cy="456" r="7" fill="#fff" stroke="#4c5a6b" stroke-width="3.5"/>
    <rect x="877" y="385" width="92" height="40" rx="3" fill="#4c5a6b"/><path d="M916 425h12l-6 6z" fill="#4c5a6b"/>
    <text x="923" y="410" fill="#fff" font-size="14" font-weight="500" text-anchor="middle" font-family="Roboto,sans-serif">$140.00</text>
    <g font-family="Roboto,sans-serif" font-size="14">
      <text x="497" y="421" fill="#4a505a">$150</text><text x="497" y="471" fill="#4a505a">$140</text>
      <text x="497" y="521" fill="#4a505a">$130</text><text x="497" y="571" fill="#1eb30e">$120</text>
      <text x="497" y="621" fill="#e8120c">$-49.98</text>
      <text x="578" y="503" fill="#2aa7e0">Averege Open Balance</text>
    </g>
  </svg>
  <div class="abs nav" style="left:557px;top:695px">‹</div>
  <div class="abs nav" style="left:1498px;top:695px">›</div>
  <div class="abs month" style="left:669px;top:700px">JAN</div>
  <div class="abs month" style="left:790px;top:700px">FEB</div>
  <div class="abs month" style="left:929px;top:700px">MARCH</div>
  <div class="abs month" style="left:1047px;top:700px">APRIL</div>
  <div class="abs month" style="left:1160px;top:700px">MAY</div>
  <div class="abs month" style="left:1286px;top:700px">JUNE</div>
  <div class="abs month" style="left:1402px;top:700px">JULY</div>
  <div class="abs tag" style="left:496px;top:740px;width:62px;background:#4cb6ea;color:#1f3a5a">PAID</div>
  <div class="abs badge b-paid" style="left:648px;top:740px;width:65px">Paid</div>
  <div class="abs badge b-partial" style="left:768px;top:740px;width:65px">Partial</div>
  <div class="abs badge b-partial" style="left:768px;top:765px;width:115px">225 Days Late</div>
  <div class="abs badge b-paid" style="left:897px;top:740px;width:65px">Paid</div>
  <div class="abs badge b-unpaid" style="left:1018px;top:740px;width:75px">Un Paid</div>
  <div class="abs badge b-partial" style="left:1018px;top:765px;width:115px">135 Days Late</div>
  <div class="abs badge b-paid" style="left:1140px;top:740px;width:65px">Paid</div>
  <div class="abs badge b-paid" style="left:1265px;top:740px;width:65px">Paid</div>
  <div class="abs badge b-partial" style="left:1381px;top:740px;width:65px">Partial</div>
  <div class="abs badge b-partial" style="left:1381px;top:765px;width:115px">225 Days Late</div>

  <!-- Extra after credits -->
  <section class="abs panel" style="left:488px;top:820px;width:339px;height:354px">
    <div class="panel-head" style="padding-left:30px">EXTRA AFTER CREDITS <span class="small" style="color:#9aa3ae;margin-left:14px;letter-spacing:.5px">JANUARY</span></div>
  </section>
  <svg class="abs" style="left:786px;top:843px" width="10" height="6"><path d="M0 0h10L5 6z" fill="#3fb6ea"/></svg>
  <div class="abs big" style="left:523px;top:900px">$2802.86</div>
  <div class="abs big" style="left:685px;top:900px">$14118</div>
  <div class="abs legend" style="left:527px;top:941px;color:#4a505a"><i style="background:#7fd0f0"></i>BALANCE</div>
  <div class="abs legend" style="left:686px;top:941px;color:#f8a900"><i style="background:#f8a900"></i>AFTER CREDITS</div>

  <!-- Payment received -->
  <section class="abs panel" style="left:848px;top:820px;width:339px;height:354px">
    <div class="panel-head" style="padding-left:30px">PAYMENT RECEIVED <span class="small" style="color:#9aa3ae;margin-left:36px;letter-spacing:.5px">JANUARY</span></div>
  </section>
  <svg class="abs" style="left:1146px;top:843px" width="10" height="6"><path d="M0 0h10L5 6z" fill="#3fb6ea"/></svg>
  <div class="abs big" style="left:883px;top:900px">$2802.86</div>
  <div class="abs big" style="left:1045px;top:900px">$1243.22</div>
  <div class="abs legend" style="left:887px;top:941px;color:#b24cf5"><i style="background:#b24cf5"></i>BALANCE</div>
  <div class="abs legend" style="left:1046px;top:941px;color:#36d9a0"><i style="background:#36f0b5"></i>PAYMENT RECEIVED</div>

  <svg class="abs" style="left:0;top:0" width="1800" height="1200" viewBox="0 0 1800 1200" font-family="Roboto,sans-serif">
    <g stroke="#e6ebf0" stroke-dasharray="3 3"><path d="M518 995H797M518 1035H797M878 995H1170M878 1035H1170"/></g>
    <path d="M518 1018C540 1005 560 1010 590 1020C640 1036 660 1040 700 1040C740 1040 750 1058 797 1060V1128H518Z" fill="#fde3a6"/>
    <path d="M518 1072C545 1040 560 1005 600 1005C640 1005 660 1050 720 1055C760 1058 780 1055 797 1055V1128H518Z" fill="#7fcbe9" opacity=".9"/>
    <circle cx="577" cy="1012" r="4" fill="#fff" stroke="#4c5a6b" stroke-width="2"/>
    <rect x="548" y="971" width="58" height="24" rx="3" fill="#4c5a6b"/><path d="M571 995h12l-6 5z" fill="#4c5a6b"/>
    <text x="577" y="987" fill="#fff" font-size="11" font-weight="500" text-anchor="middle">$14118</text>
    <g font-size="11" fill="#5a626e" font-weight="500" text-anchor="middle">
      <text x="524" y="1153">20</text><text x="569" y="1153">21</text><text x="616" y="1153">22</text><text x="661" y="1153">23</text><text x="707" y="1153">24</text><text x="751" y="1153">25</text><text x="796" y="1153">26</text>
      <text x="884" y="1153">20</text><text x="929" y="1153">21</text><text x="976" y="1153">22</text><text x="1021" y="1153">23</text><text x="1067" y="1153">24</text><text x="1111" y="1153">25</text><text x="1156" y="1153">26</text>
    </g>
    <g fill="#b24cf5">
      <rect x="889" y="1035" width="24" height="91"/><rect x="948" y="1063" width="10" height="63"/><rect x="971" y="1039" width="24" height="87"/><rect x="1028" y="1012" width="8" height="114"/><rect x="1078" y="1052" width="8" height="74"/><rect x="1121" y="1034" width="8" height="92"/><rect x="1164" y="1018" width="6" height="108"/>
    </g>
    <g fill="#36f5b3">
      <rect x="880" y="1051" width="24" height="75"/><rect x="926" y="1016" width="24" height="110"/><rect x="967" y="1078" width="22" height="48"/><rect x="1006" y="988" width="24" height="138"/><rect x="1056" y="1036" width="24" height="90"/><rect x="1099" y="1015" width="24" height="111"/><rect x="1142" y="1002" width="24" height="124"/>
    </g>
    <circle cx="937" cy="1012" r="4" fill="#fff" stroke="#4c5a6b" stroke-width="2"/>
    <rect x="908" y="971" width="58" height="24" rx="3" fill="#4c5a6b"/><path d="M931 995h12l-6 5z" fill="#4c5a6b"/>
    <text x="937" y="987" fill="#fff" font-size="11" font-weight="500" text-anchor="middle">$1243.22</text>
  </svg>

  <!-- Wallet -->
  <section class="abs panel" style="left:1208px;top:820px;width:339px;height:354px">
    <div class="panel-head" style="padding-left:30px">WALLET</div>
  </section>
  <div class="abs" style="left:1228px;top:878px;display:flex;gap:11px">
    <span class="wallet-legend"><i style="background:#a8e6cf"></i>Jan</span><span class="wallet-legend"><i style="background:#2e9a78"></i>Feb</span><span class="wallet-legend"><i style="background:#6c4f8a"></i>March</span><span class="wallet-legend"><i style="background:#7aa52a"></i>Apr</span><span class="wallet-legend"><i style="background:#d8461b"></i>May</span><span class="wallet-legend"><i style="background:#4f6287"></i>June</span>
  </div>
  <div class="abs" style="left:1228px;top:901px;display:flex;gap:11px">
    <span class="wallet-legend"><i style="background:#e0252a"></i>July</span><span class="wallet-legend"><i style="background:#19d3ee"></i>Aug</span><span class="wallet-legend"><i style="background:#1d43d6"></i>Sep</span><span class="wallet-legend"><i style="background:#3cb815"></i>Oct</span><span class="wallet-legend"><i style="background:#f9d23c"></i>Nov</span><span class="wallet-legend"><i style="background:#f437e6"></i>Dec</span>
  </div>
  <svg class="abs" style="left:1266px;top:942px" width="220" height="220" viewBox="0 0 220 220">
    <g transform="rotate(-90 110 110)" fill="none" stroke-width="18">
      <circle cx="110" cy="110" r="90" stroke="#a8e6cf" stroke-dasharray="70 495.5" stroke-dashoffset="0"/>
      <circle cx="110" cy="110" r="90" stroke="#2e9a78" stroke-dasharray="46 519.5" stroke-dashoffset="-71"/>
      <circle cx="110" cy="110" r="90" stroke="#6c4f8a" stroke-dasharray="42 523.5" stroke-dashoffset="-118"/>
      <circle cx="110" cy="110" r="90" stroke="#7aa52a" stroke-dasharray="46 519.5" stroke-dashoffset="-161"/>
      <circle cx="110" cy="110" r="90" stroke="#d8461b" stroke-dasharray="40 525.5" stroke-dashoffset="-208"/>
      <circle cx="110" cy="110" r="90" stroke="#4f6287" stroke-dasharray="40 525.5" stroke-dashoffset="-249"/>
      <circle cx="110" cy="110" r="90" stroke="#e0252a" stroke-dasharray="48 517.5" stroke-dashoffset="-290"/>
      <circle cx="110" cy="110" r="90" stroke="#19d3ee" stroke-dasharray="24 541.5" stroke-dashoffset="-339"/>
      <circle cx="110" cy="110" r="90" stroke="#1d43d6" stroke-dasharray="50 515.5" stroke-dashoffset="-364"/>
      <circle cx="110" cy="110" r="90" stroke="#3cb815" stroke-dasharray="46 519.5" stroke-dashoffset="-415"/>
      <circle cx="110" cy="110" r="90" stroke="#f9d23c" stroke-dasharray="34 531.5" stroke-dashoffset="-462"/>
      <circle cx="110" cy="110" r="90" stroke="#f437e6" stroke-dasharray="32 533.5" stroke-dashoffset="-497"/>
    </g>
    <text x="110" y="123" text-anchor="middle" font-family="Roboto,sans-serif" font-size="36" font-weight="700" fill="#2f3540">2019</text>
  </svg>
  <svg class="abs" style="left:1374px;top:937px" width="80" height="32" viewBox="0 0 80 32"><rect width="79" height="26" rx="3" fill="#4c5a6b"/><path d="M6 26h10l-5 5z" fill="#4c5a6b"/><text x="39" y="18" fill="#fff" font-size="14" text-anchor="middle" font-family="Roboto,sans-serif">$2024.00</text></svg>

  <!-- Contract price panel -->
  <section class="abs panel" style="left:488px;top:1192px;width:1059px;height:495px">
    <div class="panel-head" style="padding-left:27px">MONTH OF CONTRACT PRICE , NUMBER &amp; PAYMENT OPTIONS</div>
  </section>
  <div class="abs" style="left:494px;top:1244px;font-size:16px;font-weight:500;color:#2f3540;line-height:19px">Contract<br>Price</div>
  <svg class="abs" style="left:0;top:0" width="1800" height="1700" viewBox="0 0 1800 1700" font-family="Roboto,sans-serif">
    <defs><linearGradient id="mintArea" x1="0" y1="0" x2="0" y2="1"><stop offset="0" stop-color="#4dfcc2"/><stop offset="1" stop-color="#3fd9a9"/></linearGradient></defs>
    <g stroke="#e3e8ee">
      <path d="M557 1271H1527M557 1306H1527M557 1341H1527M557 1376H1527M557 1411H1527M557 1446H1527M557 1481H1527M557 1516H1527M557 1551H1527"/>
      <path d="M557 1240V1578M640 1240V1578M726 1240V1578M815 1240V1578M912 1240V1578M1010 1240V1578M1110 1240V1578M1210 1240V1578M1310 1240V1578M1422 1240V1578M1527 1240V1578"/>
    </g>
    <path d="M557 1420C610 1420 640 1505 695 1505C760 1505 770 1375 813 1375C850 1375 855 1450 900 1450C960 1450 990 1272 1042 1272C1100 1272 1100 1505 1130 1505C1175 1505 1180 1362 1250 1362C1310 1362 1320 1478 1355 1478C1400 1478 1430 1385 1465 1385C1500 1385 1505 1472 1527 1472V1578H557Z" fill="url(#mintArea)"/>
    <circle cx="813" cy="1375" r="6" fill="#2dc596" stroke="#7ff0c9" stroke-width="3"/>
    <rect x="793" y="1281" width="150" height="74" rx="2" fill="#4c5a6b"/>
    <text x="799" y="1300" fill="#fff" font-size="14">Number:TK219-2565</text>
    <text x="799" y="1323" fill="#36f5b3" font-size="16">$100.00</text>
    <text x="799" y="1344" fill="#fff" font-size="14">PAYMENT: ACTUAL</text>
    <g font-size="14" fill="#2aa7e0">
      <text x="495" y="1309">$12.00</text><text x="495" y="1344">$263.00</text><text x="495" y="1379">$100.00</text><text x="495" y="1414">$3232.00</text>
      <text x="495" y="1449">$789.00</text><text x="495" y="1484">$564.00</text><text x="495" y="1519">$2313.00</text><text x="495" y="1554">$587.00</text>
    </g>
    <g font-size="14" fill="#4a505a" text-anchor="middle" letter-spacing=".4">
      <text x="639" y="1615">JAN</text><text x="726" y="1615">FEB</text><text x="817" y="1615">MARCH</text><text x="912" y="1615">APRIL</text><text x="1011" y="1615">MAY</text><text x="1111" y="1615">JUNE</text><text x="1211" y="1615">JULY</text><text x="1311" y="1615">AUGUST</text><text x="1421" y="1615">SEPT</text>
    </g>
    <defs>
      <g id="pdfIcon">
        <path d="M0 0h18l7 7v23H0Z" fill="#fff" stroke="#777" stroke-width="1.2"/>
        <path d="M18 0v7h7" fill="none" stroke="#777" stroke-width="1.2"/>
        <rect x="-2" y="5" width="16" height="8" fill="#d60d0d"/>
        <text x="6" y="12" fill="#fff" font-size="6" font-weight="700" text-anchor="middle">PDF</text>
        <path d="M14 14v10M10 21l4 5 4-5" fill="none" stroke="#d60d0d" stroke-width="2.4"/>
      </g>
    </defs>
    <use href="#pdfIcon" x="629" y="1643"/><use href="#pdfIcon" x="715" y="1643"/><use href="#pdfIcon" x="808" y="1643"/><use href="#pdfIcon" x="900" y="1643"/><use href="#pdfIcon" x="1000" y="1643"/><use href="#pdfIcon" x="1100" y="1643"/><use href="#pdfIcon" x="1200" y="1643"/><use href="#pdfIcon" x="1300" y="1643"/><use href="#pdfIcon" x="1410" y="1643"/>
  </svg>
  <div class="abs nav" style="left:557px;top:1595px">‹</div>
  <div class="abs nav" style="left:1497px;top:1595px">›</div>
  <div class="abs tag" style="left:496px;top:1642px;width:62px;background:var(--pdf)">PDF</div>
</div>
</body>
</html>
```